Torvel, Inc. new buisness cards - brand guide included

We need new business cards. SLEAK SIMPLE FINANCE. They must include a place for NAME, TITLE, CELL, OFFICE PHONE, EMAIL. they also must include our services across the bottom. AIR, OCEAN, FTL, LTL, EXPRESS. for reference this will be being handed to some of the most prestigious shipping companies in a america.

Target Market(s)

Finance and corporate

Contact Information for Business Card

We need new business cards. SLEAK SIMPLE FINANCE. They must include a place for NAME, TITLE, CELL, OFFICE PHONE, EMAIL. they also must include our services across the bottom. AIR, OCEAN, FTL, LTL, EXPRESS.

Requirements
Must have
• We need new business cards. SLEAK SIMPLE FINANCE. They must include a place for NAME, TITLE, CELL, OFFICE PHONE, EMAIL. they also must include our services across the bottom. AIR, OCEAN, FTL, LTL, EXPRESS.
Nice to have
• USE THE COLORS AND LOGO IN THE BRAND GUIDE :)

```html
<!DOCTYPE html>
<html lang="en">
<head>
<meta charset="utf-8">
<title>Torvel, Inc. Business Card</title>
<link href="https://fonts.googleapis.com/css2?family=Montserrat:wght@400;500;600;700&display=swap" rel="stylesheet">
<style>
  :root {
    --backdrop: #d9d9d9;
    --card: #ffffff;
    --gold: #c5b698;
    --ink: #333333;
    --rule: #d6d0c4;
  }
  * { margin: 0; padding: 0; box-sizing: border-box; }
  html, body { width: 1200px; height: 1200px; overflow: hidden; }
  body {
    background: var(--backdrop);
    font-family: "Montserrat", Arial, sans-serif;
    color: var(--ink);
    position: relative;
  }
  .card {
    position: absolute;
    left: 203px;
    width: 789px;
    height: 503px;
    background: var(--card);
    overflow: hidden;
  }
  .card--front { top: 51px; }
  .card--back { top: 641px; }

  .wordmark {
    position: absolute;
    color: var(--gold);
    font-weight: 600;
    letter-spacing: 0.06em;
    white-space: nowrap;
    line-height: 1;
  }
  .card--front .wordmark { left: 33px; top: 76px; font-size: 36px; }
  .card--back .wordmark {
    left: 0; right: 0; top: 204px;
    text-align: center; font-size: 46px;
  }

  .person { position: absolute; left: 33px; top: 240px; }
  .person__name {
    font-size: 50px; font-weight: 600; color: var(--gold);
    line-height: 1; letter-spacing: 0.01em;
  }
  .person__title {
    font-size: 20px; font-weight: 400; margin-top: 8px; letter-spacing: 0.01em;
  }

  .divider {
    position: absolute; left: 340px; top: 202px;
    width: 1px; height: 217px; background: var(--rule);
  }

  .contact { position: absolute; left: 371px; top: 0; list-style: none; }
  .contact__item {
    position: absolute; left: 0; height: 28px; width: 410px;
    display: flex; align-items: center; white-space: nowrap;
    font-size: 19.5px; font-weight: 400;
  }
  .contact__item svg { width: 26px; height: 26px; flex: none; }
  .contact__item span { margin-left: 21px; }
  .contact__item--cell { top: 224px; }
  .contact__item--office { top: 277px; }
  .contact__item--email { top: 323px; }
  .contact__item--address { top: 370px; }

  .services-band {
    position: absolute; left: 0; top: 445px;
    width: 789px; height: 58px;
  }
  .services-band__text {
    position: absolute; left: 54px; top: 445px; height: 58px;
    display: flex; align-items: center;
    color: #fff; font-size: 20px; font-weight: 600; letter-spacing: 0.3em;
    white-space: nowrap;
  }

  .map-area {
    position: absolute; left: 24px; top: 42px; width: 723px; height: 397px;
    background: radial-gradient(ellipse at 50% 45%, #f0f0f0 0%, #f5f5f5 50%, #ffffff 75%);
  }
  .tagline {
    position: absolute; left: 0; right: 0; top: 318px;
    text-align: center; color: var(--gold);
    font-size: 26px; font-weight: 600; letter-spacing: 0.3em;
    white-space: nowrap;
  }
</style>
</head>
<body>

<section class="card card--front">
  <div class="wordmark">TORVEL, INC.</div>

  <div class="person">
    <h1 class="person__name">JOHN DOE</h1>
    <p class="person__title">DIRECTOR</p>
  </div>

  <div class="divider"></div>

  <ul class="contact">
    <li class="contact__item contact__item--cell">
      <svg viewBox="0 0 26 26" aria-hidden="true">
        <circle cx="13" cy="13" r="11.5" fill="none" stroke="#c5b698" stroke-width="2"/>
        <path d="M9 7.5c-1.2.6-1.8 1.8-1.2 3.4 1.2 3 3.5 5.4 6.4 6.6 1.6.6 2.8 0 3.4-1.2l-2.1-1.8-1.4.9c-1.6-.8-2.9-2.1-3.6-3.7l.9-1.4z" fill="#c5b698"/>
      </svg>
      <span>+1 555 0142 77</span>
    </li>
    <li class="contact__item contact__item--office">
      <svg viewBox="0 0 26 26" aria-hidden="true">
        <rect x="1" y="3" width="6" height="21" rx="1.5" fill="#c5b698"/>
        <rect x="8" y="7" width="17" height="17" rx="1.5" fill="#c5b698"/>
        <rect x="14" y="9.5" width="8" height="1.6" fill="#fff"/>
        <rect x="14" y="12.5" width="8" height="1.6" fill="#fff"/>
        <g fill="#fff"><circle cx="15" cy="17" r="0.9"/><circle cx="18" cy="17" r="0.9"/><circle cx="21" cy="17" r="0.9"/><circle cx="15" cy="20" r="0.9"/><circle cx="18" cy="20" r="0.9"/><circle cx="21" cy="20" r="0.9"/></g>
      </svg>
      <span>+1 555 0198 31</span>
    </li>
    <li class="contact__item contact__item--email">
      <svg viewBox="0 0 26 26" aria-hidden="true">
        <rect x="1" y="6" width="24" height="16" fill="#c5b698"/>
        <path d="M1.5 6.5 13 15l11.5-8.5M1.5 21.5l8.5-7M24.5 21.5l-8.5-7" fill="none" stroke="#fff" stroke-width="1.3"/>
      </svg>
      <span>HELLO@TORVELINC.COM</span>
    </li>
    <li class="contact__item contact__item--address">
      <svg viewBox="0 0 26 26" aria-hidden="true">
        <path d="M13 1.5a9 9 0 0 0-9 9c0 6 9 14 9 14s9-8 9-14a9 9 0 0 0-9-9z" fill="#c5b698"/>
        <circle cx="13" cy="10.5" r="3.6" fill="#fff"/>
      </svg>
      <span>48 HARBOR LANE PORT DISTRICT</span>
    </li>
  </ul>

  <svg class="services-band" viewBox="0 0 789 58" aria-hidden="true">
    <polygon points="0,0 580,0 604,29 580,58 0,58" fill="#c5b698"/>
    <polygon points="595,0 619,0 643,29 619,58 595,58 619,29" fill="#c5b698" opacity="0.75"/>
    <polygon points="637,0 661,0 685,29 661,58 637,58 661,29" fill="#c5b698" opacity="0.55"/>
    <polygon points="679,0 703,0 727,29 703,58 679,58 703,29" fill="#c5b698" opacity="0.4"/>
    <polygon points="721,0 745,0 769,29 745,58 721,58 745,29" fill="#c5b698" opacity="0.25"/>
  </svg>
  <div class="services-band__text">AIR, OCEAN, FTL, LTL, EXPRESS</div>
</section>

<section class="card card--back">
  <div class="map-area" role="img" aria-label="Faint line-pattern world map in the background"></div>
  <div class="wordmark">TORVEL, INC.</div>
  <p class="tagline">AIR, OCEAN, FTL, LTL, EXPRESS</p>

  <svg class="services-band" viewBox="0 0 789 58" aria-hidden="true">
    <polygon points="0,0 580,0 604,29 580,58 0,58" fill="#c5b698"/>
    <polygon points="595,0 619,0 643,29 619,58 595,58 619,29" fill="#c5b698" opacity="0.75"/>
    <polygon points="637,0 661,0 685,29 661,58 637,58 661,29" fill="#c5b698" opacity="0.55"/>
    <polygon points="679,0 703,0 727,29 703,58 679,58 703,29" fill="#c5b698" opacity="0.4"/>
    <polygon points="721,0 745,0 769,29 745,58 721,58 745,29" fill="#c5b698" opacity="0.25"/>
  </svg>
</section>

</body>
</html>
```